Create a Graphic About YOURSELF and PixelHarbor

PixelHarbor would like you (designers) to create an awesome graphic to promote YOURSELF and your profile on PixelHarbor!

Your graphic should communicate your name, your services and should mention PixelHarbor.

The design should be perfect for sharing on Chatterly. Here's an example of what we'd like http://blog.pixelharbor-example.ca/article/333/pixelharbor-launches-3000-hire-me-social-design-contest

Once you submitted your design, we'd love you to share the design ('advertisement') and promote yourself and PixelHarbor to your friends and potential customers. So make your submissions great and get your friends to vote for your design by 'Liking' it on Chatterly!

Prizes:
$1500 - "PixelHarbor Community" prize awarded to the designer with the most Chatterly 'Likes'
5 x $50 for the next 5 'most liked' designs on Chatterly

$1000 - "Hire Me" prize awarded to the designer who receives the most client invites
5 x $50 for the next 5 'most invited' designers

In summary, this is a great opportunity for you to increase your exposure to PixelHarbor customers and win cash prizes. Show off your design skills and get hired by PixelHarbor customers from around the world!

Target Market(s)

Fans, friends and customers of YOU

Industry/Entity Type

Cash

Requirements
Must have
• 1) Include your PixelHarbor user name on the graphic so customers can find you in the PixelHarbor Designer Directory
2) Include the tagline "Hire Me on PixelHarbor.com!" in your graphic design.
3) Share your design's URL on our Chatterly wall at http://chatterly-example.com/pixelharbor and get your friends to 'like' your design.
Nice to have
• 1) Include a tagline that expresses your design approach/philosophy
2) Artwork dimensions: 403 x 403 px
3) You can submit more than 1 design!
Should not have
• You must own the copyright of any images you use including stock imagery.

```html
<!DOCTYPE html>
<html lang="en">
<head>
<meta charset="utf-8">
<title>Be proud of Tovak – Hire me on PixelHarbor</title>
<link rel="stylesheet" href="https://fonts.googleapis.com/css2?family=Playfair+Display:wght@700&family=Tinos:wght@400;700&family=UnifrakturMaguntia&display=swap">
<style>
  :root {
    --bg-yellow: #ffff80;
    --band-navy: #1c2a5c;
    --band-edge: #3a6fb8;
    --tag-pink: #ea78ac;
    --name-red: #a8141c;
    --name-dark: #5e0a10;
    --contact-purple: #9a0a9a;
    --ornament-blue: #5d95d8;
    --ornament-light: #a9c9ef;
    --figure-pink: #f07ab8;
    --figure-light: #f8b6da;
    --brand-ink: #2a3d55;
    --brand-dot: #1e8fb0;
  }
  * { margin: 0; padding: 0; box-sizing: border-box; }
  html, body { width: 1200px; height: 1197px; overflow: hidden; }
  body { background: var(--bg-yellow); }
  .poster {
    position: relative;
    width: 1200px;
    height: 1197px;
    background: var(--bg-yellow);
    overflow: hidden;
  }
  .floral-ornament {
    position: absolute;
    left: 27px;
    top: 0;
    width: 880px;
    height: 480px;
  }
  .tag-band {
    position: absolute;
    left: 553px;
    top: 256px;
    width: 647px;
    height: 150px;
    background: linear-gradient(90deg, var(--band-edge) 0%, var(--band-navy) 12%, var(--band-navy) 100%);
  }
  .tagline {
    position: absolute;
    font-family: "Tinos", "Times New Roman", serif;
    font-weight: 700;
    color: var(--tag-pink);
    line-height: 1;
  }
  .tagline-be { left: 628px; top: 316px; font-size: 74px; }
  .tagline-proud { left: 712px; top: 262px; font-size: 82px; }
  .tagline-of { left: 818px; top: 336px; font-size: 70px; }
  .designer-name {
    position: absolute;
    left: 586px;
    top: 392px;
    width: 610px;
    text-align: center;
    font-family: "Playfair Display", "Times New Roman", serif;
    font-weight: 700;
    font-size: 190px;
    line-height: 1;
    color: var(--name-red);
    text-shadow: 3px 3px 0 var(--name-dark);
  }
  .designer-name-reflection {
    position: absolute;
    left: 586px;
    top: 582px;
    width: 610px;
    height: 72px;
    overflow: hidden;
    opacity: 0.25;
  }
  .designer-name-reflection span {
    display: block;
    width: 610px;
    text-align: center;
    font-family: "Playfair Display", "Times New Roman", serif;
    font-weight: 700;
    font-size: 190px;
    line-height: 1;
    color: var(--name-red);
    transform-origin: 0 0;
    transform: translateY(84px) scaleY(-0.5);
  }
  .contact-email {
    position: absolute;
    left: 600px;
    top: 690px;
    width: 596px;
    text-align: center;
    font-family: "Tinos", "Times New Roman", serif;
    font-weight: 700;
    font-size: 46px;
    color: var(--contact-purple);
  }
  .hire-line {
    position: absolute;
    left: 600px;
    width: 596px;
    text-align: center;
    font-family: "UnifrakturMaguntia", "Old English Text MT", serif;
    color: var(--contact-purple);
    line-height: 1;
  }
  .hire-so { top: 762px; font-size: 80px; }
  .hire-me { top: 830px; font-size: 100px; }
  .hire-on { top: 948px; font-size: 80px; }
  .brand-mark {
    position: absolute;
    left: 610px;
    top: 1075px;
    width: 580px;
    display: flex;
    align-items: center;
    justify-content: center;
    gap: 16px;
  }
  .brand-dot {
    width: 56px;
    height: 56px;
    border-radius: 50%;
    background: var(--brand-dot);
  }
  .brand-name {
    font-family: "Tinos", "Times New Roman", serif;
    font-weight: 700;
    font-size: 66px;
    color: var(--brand-ink);
    line-height: 1;
  }
  .walking-figures {
    position: absolute;
    left: 13px;
    top: 431px;
    width: 530px;
    height: 766px;
  }
</style>
</head>
<body>
  <main class="poster">
    <svg class="floral-ornament" viewBox="0 0 880 480" role="img" aria-label="Blue swirling floral ornament with leaves and blossoms">
      <defs>
        <radialGradient id="ornamentTone" cx="50%" cy="50%" r="50%">
          <stop offset="0%" stop-color="var(--ornament-blue)" stop-opacity="0.9"/>
          <stop offset="65%" stop-color="var(--ornament-light)" stop-opacity="0.6"/>
          <stop offset="100%" stop-color="var(--bg-yellow)" stop-opacity="0"/>
        </radialGradient>
      </defs>
      <ellipse cx="440" cy="235" rx="420" ry="225" fill="url(#ornamentTone)"/>
    </svg>

    <div class="tag-band"></div>
    <span class="tagline tagline-be">Be</span>
    <span class="tagline tagline-proud">proud</span>
    <span class="tagline tagline-of">of</span>

    <h1 class="designer-name">Tovak</h1>
    <div class="designer-name-reflection" aria-hidden="true"><span>Tovak</span></div>

    <p class="contact-email">tovakstudio@example.com</p>
    <p class="hire-line hire-so">so</p>
    <p class="hire-line hire-me">Hire me</p>
    <p class="hire-line hire-on">on</p>

    <div class="brand-mark">
      <span class="brand-dot"></span>
      <span class="brand-name">PixelHarbor</span>
    </div>

    <svg class="walking-figures" viewBox="0 0 530 766" role="img" aria-label="Pink silhouette of a father walking hand in hand with a young girl">
      <defs>
        <linearGradient id="figureTone" x1="0" y1="0" x2="0" y2="1">
          <stop offset="0%" stop-color="var(--figure-pink)"/>
          <stop offset="100%" stop-color="var(--figure-light)"/>
        </linearGradient>
      </defs>
      <rect x="200" y="0" width="300" height="766" rx="120" fill="url(#figureTone)"/>
      <rect x="0" y="300" width="230" height="466" rx="90" fill="url(#figureTone)"/>
    </svg>
  </main>
</body>
</html>
```